Inspiration Poster

Inspirational Poster that has a Kamran Dulo like abstract look (http://www.vexalo.com/images/search?q=kamran+dulo&FORM=HDRSC2) with the text:

"we walk not in order to arrive at the promise land but because walking itself is a revolution"
-Peter Ambrick

```html
<!DOCTYPE html>
<html lang="en">
<head>
<meta charset="utf-8">
<title>Inspiration Poster – Walking Is the Revolution</title>
<link rel="stylesheet" href="https://fonts.googleapis.com/css2?family=Alegreya:wght@400;500&display=swap">
<style>
  :root {
    --bg-top: #3f1c29;
    --bg-mid: #5a1c27;
    --bg-bottom: #7c1a21;
    --glow: rgba(150, 70, 90, 0.28);
    --ink-light: #ffffff;
    --ink-author: #5c1519;
  }
  html, body {
    margin: 0;
    padding: 0;
    width: 848px;
    height: 1200px;
    overflow: hidden;
    background: var(--bg-bottom);
  }
  .poster {
    position: relative;
    width: 848px;
    height: 1200px;
    overflow: hidden;
    background:
      radial-gradient(ellipse 260px 200px at 640px 640px, var(--glow), transparent 70%),
      radial-gradient(ellipse 300px 220px at 170px 480px, rgba(120, 60, 80, 0.22), transparent 70%),
      radial-gradient(ellipse 240px 180px at 720px 180px, rgba(110, 60, 80, 0.2), transparent 70%),
      linear-gradient(180deg, var(--bg-top) 0%, var(--bg-mid) 45%, var(--bg-bottom) 100%);
  }
  .poster__type {
    position: absolute;
    inset: 0;
    width: 848px;
    height: 1200px;
  }
  .quote {
    font-family: "Alegreya", Georgia, serif;
    fill: var(--ink-light);
    filter: drop-shadow(0 0 3px rgba(255, 255, 255, 0.35));
  }
  .quote__rule { stroke: var(--ink-light); stroke-width: 2.5; }
  .author {
    font-family: "Alegreya", Georgia, serif;
    fill: var(--ink-author);
  }
</style>
</head>
<body>
  <main class="poster">
    <svg class="poster__type" viewBox="0 0 848 1200" xmlns="http://www.w3.org/2000/svg">
      <g class="quote" aria-label="We walk not in order to arrive at a promise land but because walking itself is the revolution.">
        <text x="168" y="232" font-size="104" textLength="495" lengthAdjust="spacingAndGlyphs">We walk</text>
        <text x="102" y="340" font-size="172" textLength="298" lengthAdjust="spacingAndGlyphs">NOT</text>
        <text x="410" y="286" font-size="58" textLength="253" lengthAdjust="spacingAndGlyphs">in order</text>
        <text x="410" y="340" font-size="58" textLength="253" lengthAdjust="spacingAndGlyphs">to arrive</text>
        <text x="100" y="425" font-size="60" textLength="478" lengthAdjust="spacingAndGlyphs">at a PROMISE</text>
        <line class="quote__rule" x1="232" y1="435" x2="578" y2="435"/>
        <text x="223" y="553" font-size="180" textLength="345" lengthAdjust="spacingAndGlyphs">LAN</text>
        <text x="566" y="553" font-size="300" textLength="182" lengthAdjust="spacingAndGlyphs">D</text>
        <text x="210" y="592" font-size="44" textLength="98" lengthAdjust="spacingAndGlyphs">but</text>
        <text x="397" y="598" font-size="46" textLength="181" lengthAdjust="spacingAndGlyphs">because</text>
        <text x="168" y="658" font-size="104" textLength="400" lengthAdjust="spacingAndGlyphs">walking</text>
        <text x="252" y="726" font-size="50" textLength="128" lengthAdjust="spacingAndGlyphs">itself</text>
        <text x="289" y="771" font-size="50" textLength="42" lengthAdjust="spacingAndGlyphs">is</text>
        <text x="397" y="771" font-size="110" textLength="181" lengthAdjust="spacingAndGlyphs">the</text>
        <text x="25" y="907" font-size="120" textLength="801" lengthAdjust="spacingAndGlyphs">REVOLUTION.</text>
      </g>
      <g class="author" aria-label="Peter Ambrick">
        <text x="400" y="1077" font-size="56" textLength="172" lengthAdjust="spacingAndGlyphs">Peter</text>
        <text x="304" y="1125" font-size="36" textLength="264" lengthAdjust="spacingAndGlyphs">AMBRICK</text>
      </g>
    </svg>
  </main>
</body>
</html>
```